TK Drafting

Simple Design - Logo is done (from this site). Logo on one side - Back Side an image or outline of a house blue print - My name, phone, email, website url. Prefer the traditional Architectural style of letters -

Target Market(s)

Customers who need a floor plan redesigned for renovations or realtors who want a floor plan for marketing their listings

Industry/Entity Type

Architecture

Contact Information for Business Card

Colin Varga - Name
318-542-6604 - Phone
tkdraftingco@mailvane.com
www.tkdraftingco.net

Font styles to use
Other font styles liked:
• Architecture writing -

Colors
0555a3
3276b5
85acd3

Requirements
Must have
• Logo that is attached. I like an indigo blue color for the background or a royal blue - gray logo OR - white and clean with the logo on one side and the same color gray lettering on the other side
Nice to have
• some sort of image that shows a residential blue print. It may not be possible on this small of a card though.
Should not have
• Nothing cartoonish.

```html
<!DOCTYPE html>
<html lang="en">
<head>
<meta charset="utf-8">
<title>TK Drafting Business Card</title>
<link href="https://fonts.googleapis.com/css2?family=Open+Sans:wght@400;700&display=swap" rel="stylesheet">
<style>
  :root {
    --stage: #3a3a3a;
    --card: #1c1c1e;
    --card-back: #141415;
    --pattern-light: #2c2c2f;
    --pattern-dark: #0e0e0f;
    --edge-blue: #3276b5;
    --name-blue: #3276b5;
    --text-light: #e6e6ea;
    --mark-gray: #b9b9c0;
    --mark-white: #e8e8ec;
    --divider: #2b5f95;
  }
  * { box-sizing: border-box; margin: 0; padding: 0; }
  html, body { width: 1200px; height: 801px; overflow: hidden; }
  body {
    background: var(--stage);
    font-family: "Open Sans", Arial, sans-serif;
    display: flex;
    align-items: center;
    justify-content: center;
    gap: 40px;
  }
  .card {
    position: relative;
    width: 540px;
    height: 309px;
    border-right: 3px solid var(--edge-blue);
    border-bottom: 3px solid var(--edge-blue);
    overflow: hidden;
  }
  .card-front { background: var(--card); }
  .card-back { background: var(--card-back); }

  .brand {
    position: absolute;
    left: 0; top: 0;
    width: 250px; height: 100%;
    display: flex;
    align-items: center;
    justify-content: center;
    gap: 10px;
  }
  .brand-square {
    width: 14px; height: 14px;
    background: var(--mark-gray);
  }
  .brand-name {
    color: var(--mark-gray);
    font-weight: 700;
    font-size: 26px;
    letter-spacing: 1px;
    white-space: nowrap;
  }
  .divider {
    position: absolute;
    left: 256px; top: 104px;
    width: 1px; height: 104px;
    background: var(--divider);
  }
  .contact {
    position: absolute;
    left: 278px; top: 72px;
  }
  .contact-name {
    color: var(--name-blue);
    font-weight: 700;
    font-size: 20px;
    letter-spacing: 0.5px;
    text-transform: uppercase;
    margin-bottom: 18px;
  }
  .contact-line {
    display: flex;
    align-items: center;
    gap: 8px;
    color: var(--text-light);
    font-size: 15px;
    line-height: 26px;
    white-space: nowrap;
  }
  .contact-line svg { width: 11px; height: 11px; fill: var(--edge-blue); flex: none; }

  .pattern-field {
    position: absolute;
    inset: 0;
    background:
      radial-gradient(ellipse at 72% 50%, var(--pattern-light) 0%, #1d1d1f 45%, var(--pattern-dark) 100%);
  }
  .back-brand {
    position: absolute;
    left: 300px; top: 0;
    height: 100%;
    display: flex;
    align-items: center;
    gap: 8px;
  }
  .back-brand .brand-square { background: var(--mark-white); width: 12px; height: 12px; }
  .back-brand .brand-name { color: var(--mark-white); font-size: 22px; }
</style>
</head>
<body>
  <section class="card card-front">
    <div class="brand">
      <span class="brand-square"></span>
      <span class="brand-name">TK Drafting</span>
    </div>
    <div class="divider"></div>
    <div class="contact">
      <p class="contact-name">Colin Varga</p>
      <p class="contact-line">
        <svg viewBox="0 0 12 12"><path d="M2.5 1 L4.5 1 L5 3.5 L3.8 4.5 C4.5 6 6 7.5 7.5 8.2 L8.5 7 L11 7.5 L11 9.5 C11 10.5 10 11 9 11 C4.5 10.5 1.5 7.5 1 3 C1 2 1.5 1 2.5 1 Z"/></svg>
        318-542-6604
      </p>
      <p class="contact-line">
        <svg viewBox="0 0 12 12"><path d="M1 2.5 H11 V9.5 H1 Z M1.5 3 L6 6.5 L10.5 3 V3.5 L6 7.2 L1.5 3.5 Z" fill-rule="evenodd"/></svg>
        tkdraftingco@mailvane.com
      </p>
      <p class="contact-line">
        <svg viewBox="0 0 12 12"><circle cx="6" cy="6" r="5"/></svg>
        www.tkdraftingco.net
      </p>
    </div>
  </section>

  <section class="card card-back">
    <div class="pattern-field" role="img" aria-label="Tone-on-tone repeating brand pattern in black gloss covering the card back"></div>
    <div class="back-brand">
      <span class="brand-square"></span>
      <span class="brand-name">TK Drafting</span>
    </div>
  </section>
</body>
</html>
```